Evergrove Yard Service and Beyond LLC

• Mowing
• Weed eating
•Edging
• hedge trimming
• landscaping
•mulching
•yard clean up
• pressure washing

Target Market(s)

Everyone

Contact Information for Business Card

Licensed and insured

Font styles to use
Serif

Colors
59FF00
82FF00
B8FF75
E3FFCB
F4FFEA
F0912C
F2A743
F7CA91
FBE8D2
FDF5EE
EE7325
F08F49
F5BC92
FAE3D3
FDF4ED
EB3D1F
EC4F4E
F09395
F8D3D4
FCEDEE
E54698
E96AAD
F1A4CE
F9D9EA
FCEFF6

```html
<!DOCTYPE html>
<html lang="en">
<head>
<meta charset="utf-8">
<title>Evergrove Yard Service and Beyond LLC – Business Card</title>
<link rel="stylesheet" href="https://fonts.googleapis.com/css2?family=Montserrat:wght@400;500;600;700&display=swap">
<style>
  :root {
    --backdrop: #6e5538;
    --card: #262626;
    --brand-green: #1f9a42;
    --lime: #8cc63f;
    --deep-green: #16963f;
    --text-light: #f2f2f2;
    --leaf-shade: #4a4a4a;
  }
  * { box-sizing: border-box; margin: 0; padding: 0; }
  html, body { width: 900px; height: 1200px; overflow: hidden; }
  body {
    background: var(--backdrop);
    font-family: "Montserrat", sans-serif;
    color: var(--text-light);
    position: relative;
  }
  .card {
    position: absolute;
    left: 80px;
    width: 742px;
    height: 440px;
    background: var(--card);
    border-radius: 28px;
    overflow: hidden;
    box-shadow: 0 6px 14px rgba(0,0,0,.45);
  }
  .card--front { top: 132px; }
  .card--back { top: 640px; }

  .brand-name {
    position: absolute;
    color: var(--brand-green);
    font-weight: 700;
    text-align: center;
    line-height: 1.15;
  }
  .brand-name .brand-main { display: block; font-size: 42px; letter-spacing: 2px; }
  .brand-name .brand-sub { display: block; font-size: 19px; letter-spacing: 1px; }
  .card--front .brand-name { left: 36px; top: 56px; width: 410px; }
  .card--back .brand-name { left: 48px; top: 66px; width: 520px; }
  .card--back .brand-name .brand-main { font-size: 50px; }
  .card--back .brand-name .brand-sub { font-size: 23px; }

  .leaf-motif {
    position: absolute;
    background: radial-gradient(ellipse at 60% 55%, #444 0%, #333 45%, rgba(38,38,38,0) 75%);
  }
  .card--front .leaf-motif { left: 300px; top: 160px; width: 460px; height: 230px; }
  .card--back .leaf-motif { left: 220px; top: 110px; width: 540px; height: 330px; }

  .holder { position: absolute; left: 40px; top: 186px; }
  .holder-name { color: var(--brand-green); font-size: 26px; font-weight: 700; }
  .holder-role { font-size: 18px; margin-top: 2px; }

  .contact-list { position: absolute; left: 44px; top: 256px; list-style: none; }
  .contact-list li { display: flex; align-items: center; font-size: 18px; height: 26px; }
  .contact-list svg { width: 16px; height: 16px; margin-right: 12px; fill: var(--brand-green); }

  .address { position: absolute; left: 46px; top: 348px; font-size: 18px; line-height: 22px; }

  .badge-band { position: absolute; left: 0; top: 384px; width: 742px; height: 56px; }
  .badge-text {
    position: absolute; right: 26px; top: 404px;
    font-size: 18px; font-weight: 500; color: #fff;
  }

  .services-title {
    position: absolute; left: 34px; top: 174px;
    color: var(--brand-green); font-size: 22px; font-weight: 600;
  }
  .services-list { position: absolute; left: 36px; top 0; top: 216px; list-style: none; }
  .services-list li {
    font-size: 20px; height: 23px; line-height: 23px;
    display: flex; align-items: center;
  }
  .services-list li::before {
    content: ""; width: 10px; height: 10px; border-radius: 50%;
    background: var(--lime); margin-right: 7px;
  }
</style>
</head>
<body>

<section class="card card--front">
  <div class="brand-name">
    <span class="brand-main">EVERGROVE</span>
    <span class="brand-sub">YARD SERVICE &amp; BEYOND LLC</span>
  </div>

  <div class="leaf-motif" role="img" aria-label="Large soft leaf decoration"></div>

  <div class="holder">
    <div class="holder-name">Daniel Hartwell</div>
    <div class="holder-role">Owner</div>
  </div>

  <ul class="contact-list">
    <li>
      <svg viewBox="0 0 16 16" aria-hidden="true"><path d="M3 3c1-1 2-1 3 0l1 2c.4.6.2 1.2-.3 1.6l-.8.6c.8 1.6 2 2.8 3.6 3.6l.6-.8c.4-.5 1-.7 1.6-.3l2 1c1 1 1 2 0 3-1.5 1.5-4 1-7-2S1.5 4.5 3 3z"/></svg>
      (555) 014-2290
    </li>
    <li>
      <svg viewBox="0 0 16 16" aria-hidden="true"><path d="M1 4h14v9H1z M1 4l7 5 7-5" stroke="#262626" stroke-width="1.2"/></svg>
      hello@evergroveyard.com
    </li>
    <li>
      <svg viewBox="0 0 16 16" aria-hidden="true"><circle cx="8" cy="8" r="7"/><path d="M1 8h14M8 1c-3 3-3 11 0 14M8 1c3 3 3 11 0 14" stroke="#262626" stroke-width="1" fill="none"/></svg>
      www.evergroveyard.com
    </li>
  </ul>

  <div class="address">482 Maple Row, Brookfield<br>State, 55555</div>

  <svg class="badge-band" viewBox="0 0 742 56" aria-hidden="true">
    <polygon points="0,38 400,38 400,56 0,56" fill="var(--lime)"/>
    <polygon points="420,0 496,0 462,52 386,52 400,38" fill="var(--lime)"/>
    <polygon points="510,0 742,0 742,56 474,56" fill="var(--deep-green)"/>
    <path d="M428 26 l8 8 l16 -18" stroke="#fff" stroke-width="5" fill="none" stroke-linecap="round" stroke-linejoin="round"/>
  </svg>
  <div class="badge-text">Licensed and insured</div>
</section>

<section class="card card--back">
  <div class="brand-name">
    <span class="brand-main">EVERGROVE</span>
    <span class="brand-sub">YARD SERVICE &amp; BEYOND LLC</span>
  </div>

  <div class="leaf-motif" role="img" aria-label="Large soft leaf decoration"></div>

  <h2 class="services-title">Our Services</h2>
  <ul class="services-list">
    <li>Mowing</li>
    <li>Weed eating</li>
    <li>Edging</li>
    <li>Hedge trimming</li>
    <li>Landscaping</li>
    <li>Mulching</li>
    <li>Yard clean up</li>
    <li>Pressure washing</li>
  </ul>
</section>

</body>
</html>
```